Targeting Judges,Attorneys,People facing alcohol related charges dui etc.
Our state fo the art technology uses portable breathalyzer that bluetooths to our Q-Link ORB app installed on smartphones both iphone and android
to monitor 24/7 sobriety. We use biometrics, video checkins, agency notifications,Gps tracking. Low cost method for judicial authorities to see more information for enhanced monitoring and supervision, to have a much better sense of where their offenders go, behavioral patterns and potential downfalls to their sucess. This data can assist officials in assessing and influencing the criminogenic environment of each offender.
colors scheme should use blues navey . design should communicate to the Justice system this new technology

See tunevault and app bazaar app links
also link to our website q-link.example

Target Market(s)

Judicial System

Font styles to use
Sans Serif

Colors
3276b5

Requirements
Must have
• Logo,links to app stores, 1-888-555-0147,q-link.example,picture of smartphone and alcohol monitor, Introducing Q-Link ORB 24/7 Sobriety monitoring

```html
<!DOCTYPE html>
<html lang="en">
<head>
<meta charset="utf-8">
<title>Q-Link ORB 24/7 Sobriety Monitoring – Trifold</title>
<link rel="stylesheet" href="https://fonts.googleapis.com/css2?family=Montserrat:wght@400;500;600;700&display=swap">
<style>
  :root{
    --page:#e9eef3;
    --navy:#0c2f7a;
    --blue:#3276b5;
    --blue-deep:#1b4f93;
    --charcoal:#3a3a3c;
    --charcoal-dark:#1f1f21;
    --lime:#c8e03a;
    --white:#ffffff;
    --ink-soft:#e6ecf5;
  }
  *{box-sizing:border-box;margin:0;padding:0}
  html,body{width:1200px;height:1200px;overflow:hidden;background:var(--page);font-family:"Montserrat",sans-serif;color:var(--white)}
  .brochure{position:absolute;left:0;top:177px;width:1200px;height:846px;overflow:hidden}
  .panel{position:absolute;top:0;height:846px}
  .panel-left{left:0;width:398px}
  .panel-middle{left:398px;width:402px}
  .panel-right{left:800px;width:400px}
  .panel-backdrop{position:absolute;inset:0}
  .panel-left .panel-backdrop{background:linear-gradient(160deg,#8b9099 0%,#5d7fae 22%,var(--blue) 45%,var(--blue-deep) 100%)}
  .panel-middle .panel-backdrop{background:linear-gradient(180deg,var(--charcoal) 0%,#4a4a4d 45%,var(--charcoal-dark) 100%)}
  .panel-right .panel-backdrop{background:linear-gradient(200deg,#b9bcc2 0%,#4a72aa 25%,var(--blue-deep) 55%,#0d1d3c 100%)}
  .bottom-band{position:absolute;left:0;bottom:0;width:1200px;height:16px;background:var(--navy)}
  .abs{position:absolute}

  /* left panel */
  .brand-mark{left:123px;top:66px;width:152px;height:152px;background:var(--navy);display:flex;align-items:center;justify-content:center}
  .brand-mark span{font-weight:700;font-size:19px;color:var(--white);letter-spacing:.5px}
  .cover-kicker{left:20px;width:358px;top:234px;text-align:center;font-weight:600;font-size:14px;letter-spacing:3px;color:var(--lime)}
  .cover-title{left:14px;width:370px;top:256px;text-align:center;font-weight:700;font-size:25px;line-height:33px;text-transform:uppercase}
  .cover-tagline{left:40px;width:318px;top:342px;text-align:center;font-weight:700;font-size:14px;line-height:17px}
  .how-button{left:88px;top:418px;width:222px;height:47px;border:3px solid var(--lime);display:flex;align-items:center;justify-content:center;font-size:22px;font-weight:400;letter-spacing:.3px}
  .body-copy{left:46px;top:482px;width:309px;font-size:11px;line-height:13.7px;text-align:justify;color:var(--ink-soft)}
  .body-copy p{margin-bottom:6px}

  /* middle panel */
  .section-title{left:0;width:402px;text-align:center;font-weight:700;font-size:32px;letter-spacing:.5px}
  .feature{left:0;width:402px;text-align:center}
  .feature-icon{display:block;margin:0 auto 8px;width:66px;height:66px}
  .feature h3{color:var(--lime);font-size:15.5px;font-weight:600;margin-bottom:6px}
  .feature p{font-size:11px;color:#e4e4e4}
  .advantage-list{left:0;width:402px;top:660px;text-align:center;list-style:none;font-size:14px;font-weight:600;line-height:17px}

  /* right panel */
  .flow-diagram{left:848px;top:86px;width:307px;height:174px;border:1px solid var(--white);background:linear-gradient(180deg,var(--navy),#183f86)}
  .app-title{left:848px;top:300px;font-weight:700;font-size:24px;line-height:30px;text-transform:uppercase}
  .store-badge{left:847px;width:106px;height:30px;background:#000;border:1px solid #9a9a9a;border-radius:5px}
  .app-screen{left:1022px;top:280px;width:133px;height:232px;border:2px solid var(--white);border-radius:4px;background:linear-gradient(180deg,#2b57b8 0 12%,#5aa3dc 12%,#4f93d3 100%)}
  .signup-note{left:860px;width:270px;top:524px;text-align:center;font-size:11px;font-weight:600}
  .contact{left:850px;width:300px;text-align:center;font-weight:600}
  .contact svg{display:block;margin:0 auto 6px}
  .contact-text{font-size:16px;line-height:21px}
</style>
</head>
<body>
<main class="brochure">

  <section class="panel panel-left">
    <div class="panel-backdrop" role="img" aria-label="Upward view of glass office towers tinted in blue"></div>
    <div class="abs brand-mark"><span>Q-Link ORB</span></div>
    <p class="abs cover-kicker">INTRODUCING</p>
    <h1 class="abs cover-title">Q-Link ORB 24/7<br>Sobriety Monitoring</h1>
    <p class="abs cover-tagline">Portable Bluetooth Breathalyzer + Smartphone App--Enhanced Supervision for Courts!</p>
    <div class="abs how-button">HOW IT WORKS</div>
    <div class="abs body-copy">
      <p>The Q-Link ORB is a portable breathalyzer that pairs by Bluetooth with the Q-Link ORB app on iPhone and Android smartphones. It delivers 24/7 sobriety monitoring for people facing alcohol related charges such as DUI, with biometrics, video check-ins, agency notifications and GPS tracking in one low cost system.</p>
      <p>Every breath test is confirmed with biometric identification and a video check-in, so officials know exactly who tested, when and where. Missed or failed tests trigger instant agency notifications, giving judges, attorneys and supervising officers a clear and secure record of compliance without the cost of an ankle bracelet or a lab visit.</p>
      <p>Beyond testing, the data collected shows where offenders go, their behavioral patterns and the potential downfalls to their success. This information can help officials assess and influence the criminogenic environment of each offender, and build customized programs based on the details our clients have asked to receive.</p>
    </div>
  </section>

  <section class="panel panel-middle">
    <div class="panel-backdrop" role="img" aria-label="Dark grey view of a skyscraper facade"></div>
    <h2 class="abs section-title" style="top:80px">KEY FEATURES</h2>

    <div class="abs feature" style="top:150px">
      <svg class="feature-icon" viewBox="0 0 66 66" fill="none" stroke="#fff" stroke-width="2">
        <circle cx="33" cy="33" r="31"/>
        <rect x="25" y="24" width="16" height="28" rx="4"/>
        <rect x="30" y="14" width="6" height="10" rx="1"/>
        <line x1="29" y1="32" x2="37" y2="32"/>
        <circle cx="33" cy="43" r="3"/>
      </svg>
      <h3>Bluetooth Breathalyzer Testing</h3>
      <p>Portable breath tests sent straight to the app, 24/7.</p>
    </div>

    <div class="abs feature" style="top:290px">
      <svg class="feature-icon" viewBox="0 0 66 66" fill="none" stroke="#fff" stroke-width="2">
        <circle cx="33" cy="33" r="31"/>
        <rect x="23" y="15" width="20" height="36" rx="3"/>
        <circle cx="33" cy="32" r="5"/>
        <line x1="30" y1="46" x2="36" y2="46"/>
      </svg>
      <h3>Video Check-ins &amp; GPS Tracking</h3>
      <p>Live video calls, photo check-ins and real-time location monitoring</p>
    </div>

    <div class="abs feature" style="top:425px">
      <svg class="feature-icon" viewBox="0 0 66 66" fill="none" stroke="#fff" stroke-width="2">
        <circle cx="33" cy="33" r="31"/>
        <path d="M19 36a14 14 0 0 1 28 0v6M23 44v-8a10 10 0 0 1 20 0v9M28 48V36a5 5 0 0 1 10 0v10M33 36v14"/>
      </svg>
      <h3>Biometric Identification</h3>
      <p>Fingerprint and facial recognition</p>
    </div>

    <h2 class="abs section-title" style="top:610px">ADVANTAGES</h2>
    <ul class="abs advantage-list">
      <li>Low Cost Sobriety Monitoring</li>
      <li>Instant Agency Notifications</li>
      <li>Full Training and Support</li>
    </ul>
  </section>

  <section class="panel panel-right">
    <div class="panel-backdrop" role="img" aria-label="Office towers fading from grey to deep blue"></div>
  </section>

  <div class="abs flow-diagram" role="img" aria-label="Illustration: offender using the portable breathalyzer and phone, results sent through the cloud to a monitoring agency's tablet"></div>
  <h2 class="abs app-title">Get the<br>Q-Link ORB<br>Sobriety<br>App Now!</h2>
  <div class="abs store-badge" style="top:442px" role="img" aria-label="app bazaar download badge"></div>
  <div class="abs store-badge" style="top:475px" role="img" aria-label="tunevault download badge"></div>
  <div class="abs app-screen" role="img" aria-label="App home screen with breath test, map, check-ins, profile, instructions and check-in buttons"></div>
  <p class="abs signup-note">*Sign-up Required before Activation</p>

  <div class="abs contact" style="top:594px">
    <svg width="22" height="22" viewBox="0 0 24 24" fill="var(--lime)"><path d="M6.6 10.8a15 15 0 0 0 6.6 6.6l2.2-2.2a1 1 0 0 1 1-.25 11.4 11.4 0 0 0 3.6.6 1 1 0 0 1 1 1V20a1 1 0 0 1-1 1A17 17 0 0 1 3 4a1 1 0 0 1 1-1h3.5a1 1 0 0 1 1 1c0 1.25.2 2.45.6 3.6a1 1 0 0 1-.25 1z"/></svg>
    <div class="contact-text">1.888.555.0147</div>
  </div>
  <div class="abs contact" style="top:673px">
    <svg width="24" height="18" viewBox="0 0 24 18" fill="var(--lime)"><path d="M0 0h24v18H0z"/><path d="M0 0l12 10L24 0" fill="none" stroke="#1b4f93" stroke-width="2"/></svg>
    <div class="contact-text">q-link.example</div>
  </div>
  <div class="abs contact" style="top:736px">
    <svg width="20" height="26" viewBox="0 0 20 26" fill="var(--lime)"><path d="M10 0a10 10 0 0 1 10 10c0 7-10 16-10 16S0 17 0 10A10 10 0 0 1 10 0z"/><circle cx="10" cy="10" r="4" fill="#1b4f93"/></svg>
    <div class="contact-text">418 Harbor Ave<br>Lakemont, AR 72999</div>
  </div>

  <div class="bottom-band"></div>
</main>
</body>
</html>
```